Rivet Athletic Supply Inc.

Need to create a website that is informational and has the ability to sell goods and services. Such as a custom t shirt designer where the user can upload and image to be displayed on the garmet. The sports we specialize in are basketball, football, and baseball.

Would like like:
Home Page
Locker Room Page:
Custom Uniforms Page
Custom Shirt Creator
Brands
About

Competitor websites are
lornfieldsportsco.example
qtv.example
wmdgear.example

```html
<!DOCTYPE html>
<html lang="en">
<head>
<meta charset="utf-8">
<title>Rivet Athletic Supply — Design Your Own</title>
<link href="https://fonts.googleapis.com/css2?family=Lexend:wght@400;500;600;700;800&family=Outfit:wght@300;400;500;600;700&display=swap" rel="stylesheet">
<style>
:root{
  --blue:#1a6ff0;
  --blue-dark:#0f5ad0;
  --ink:#111418;
  --muted:#6b7280;
  --line:#e5e7eb;
  --soft:#f4f5f7;
  --navy:#0f1a2e;
  --white:#ffffff;
  --red:#d6272f;
  --icon-bg:#e8f0fd;
}
*{box-sizing:border-box;margin:0;padding:0}
html,body{width:1200px;height:3809px;overflow:hidden}
body{font-family:"Outfit",sans-serif;color:var(--ink);background:var(--white);position:relative}
.heading{font-family:"Lexend",sans-serif}
section,header,footer{position:relative;width:1200px}

/* nav */
.site-nav{height:75px;border-bottom:1px solid var(--line);display:flex;align-items:center;padding:0 40px}
.brand{display:flex;align-items:center;gap:8px;font-family:"Outfit",sans-serif;font-weight:700;color:var(--blue);font-size:19px;letter-spacing:.2px}
.brand-square{width:16px;height:16px;background:var(--red);border-radius:3px}
.nav-links{position:absolute;left:384px;display:flex;gap:30px;font-size:14px;color:#2b2f36}
.btn-primary{background:var(--blue);color:var(--white);border-radius:999px;font-weight:600;display:flex;align-items:center;justify-content:center;font-size:14px}
.nav-cta{position:absolute;left:962px;top:19px;width:147px;height:36px}
.cart{position:absolute;left:1124px;top:19px;width:36px;height:36px;border-radius:50%;background:var(--soft);display:flex;align-items:center;justify-content:center}

/* hero */
.hero{height:812px}
.hero-photo{position:absolute;inset:0;background:radial-gradient(ellipse at 55% 35%,#5a3a2e 0%,#2e2420 35%,#16181a 70%,#0d0f10 100%)}
.hero-shade{position:absolute;inset:0;background:linear-gradient(90deg,rgba(0,0,0,.55) 0%,rgba(0,0,0,.15) 55%,rgba(0,0,0,.25) 100%)}
.hero-title{position:absolute;left:48px;top:236px;font-size:66px;line-height:67px;font-weight:800;color:var(--white)}
.hero-sub{position:absolute;left:47px;top:522px;width:560px;font-size:19.5px;line-height:27px;color:var(--white);font-weight:500}
.design-card{position:absolute;left:683px;top:120px;width:470px;height:574px;background:rgba(243,244,246,.96);border-radius:30px;padding:36px 38px}
.design-card h2{text-align:center;font-size:27px;line-height:34px;font-weight:700;margin-bottom:20px}
.field-label{font-size:12.5px;font-weight:600;color:#2b2f36;margin-bottom:10px}
.select{height:44px;background:var(--white);border:1px solid var(--line);border-radius:22px;display:flex;align-items:center;justify-content:space-between;padding:0 14px;font-size:14px;color:#444;margin-bottom:26px}
.colors{display:flex;gap:22px;font-size:13px;color:var(--muted);margin-bottom:26px}
.swatch{display:flex;align-items:center;gap:10px}
.swatch i{width:16px;height:16px;border-radius:3px;display:block}
.dropzone{height:120px;border:2px dashed #d6d9de;border-radius:22px;background:var(--white);display:flex;flex-direction:column;align-items:center;justify-content:center;gap:14px;font-size:12.5px;color:var(--muted)}
.drop-note{text-align:center;font-size:10.5px;color:#9aa0a8;margin:10px 0 16px}
.card-cta{height:44px;font-size:14px;box-shadow:0 6px 14px rgba(26,111,240,.3)}

/* steps */
.steps{height:402px}
.section-title{font-size:32px;font-weight:700;text-align:center}
.steps .section-title{position:absolute;top:60px;width:100%}
.step{position:absolute;top:142px;width:300px;text-align:center}
.step-icon{width:74px;height:74px;border-radius:50%;background:var(--icon-bg);margin:0 auto 28px;display:flex;align-items:center;justify-content:center}
.step h3{font-size:18px;font-weight:600;margin-bottom:12px;letter-spacing:.3px}
.step p{width:276px;margin:0 auto;font-size:14.5px;line-height:22px;color:var(--muted)}

/* gear */
.gear{height:705px;background:var(--soft)}
.gear h2{position:absolute;left:38px;top:74px;font-size:32px;font-weight:700}
.view-all{position:absolute;right:38px;top:93px;font-size:13px;color:var(--blue);font-weight:600}
.gear-card{position:absolute;top:149px;width:359px;height:479px;border-radius:12px;overflow:hidden}
.gear-card span{position:absolute;left:30px;bottom:54px;font-family:"Lexend",sans-serif;font-size:28px;font-weight:700;color:var(--white)}
.tone-basketball{background:linear-gradient(180deg,#b07c4c 0%,#8e5f36 60%,#3a2a1e 100%)}
.tone-football{background:linear-gradient(180deg,#2c3434 0%,#232a30 55%,#141618 100%)}
.tone-baseball{background:linear-gradient(135deg,#8a8480 0%,#5e5854 50%,#3a3532 100%)}

/* champions */
.champions{height:1113px}
.champions h2{position:absolute;top:72px;width:100%;font-size:32px}
.champions .lead{position:absolute;top:127px;width:100%;text-align:center;font-size:16px;color:var(--muted)}
.gallery-tile{position:absolute;width:359px;height:359px;border-radius:10px;overflow:hidden}
.tag{position:absolute;left:16px;bottom:14px;background:var(--white);border-radius:999px;font-size:10px;font-weight:600;letter-spacing:1.2px;padding:4px 12px;color:#222}
.t-basketball{background:radial-gradient(circle at 50% 40%,#4a4a4a,#1c1c1c)}
.t-track{background:linear-gradient(180deg,#6f9a5a 0%,#7aa0c0 18%,#c2593a 40%,#b44e30 100%)}
.t-hockey{background:linear-gradient(180deg,#98aab0 0%,#b8c6ca 60%,#e3e8ea 100%)}
.t-volleyball{background:linear-gradient(180deg,#2a2f3a 0%,#5a5e6a 55%,#3aa6b8 100%)}
.t-soccer{background:linear-gradient(180deg,#1d2230 0%,#22283a 60%,#6e5140 100%)}
.t-baseball{background:linear-gradient(180deg,#3f6a3a 0%,#6a8a56 45%,#b07a5a 100%)}
.btn-outline{position:absolute;left:477px;top:993px;width:246px;height:44px;border:1px solid var(--line);border-radius:999px;display:flex;align-items:center;justify-content:center;font-size:13.5px;font-weight:500;box-shadow:0 2px 6px rgba(0,0,0,.05)}

/* team band */
.team-band{height:213px;background:var(--navy);color:var(--white)}
.team-band h2{position:absolute;left:38px;top:62px;font-size:28px;font-weight:700}
.team-band p{position:absolute;left:38px;top:102px;width:500px;font-size:17px;line-height:27px;color:#c8cfdb}
.team-cta{position:absolute;left:953px;top:85px;width:209px;height:45px;font-size:14.5px}

/* footer */
.site-footer{height:489px}
.footer-brand{position:absolute;left:70px;top:46px}
.footer-about{position:absolute;left:38px;top:113px;width:260px;font-size:12.5px;line-height:18px;color:var(--muted)}
.footer-col{position:absolute;top:64px}
.footer-col h4{font-size:12px;font-weight:600;letter-spacing:1.5px;margin-bottom:14px}
.footer-col li{list-style:none;font-size:13px;color:var(--muted);line-height:29.5px}
.socials{display:flex;gap:18px;margin-bottom:16px}
.socials i{width:18px;height:18px;border-radius:4px;display:block}
.phone{font-size:13px;color:var(--muted)}
.divider{position:absolute;left:38px;right:38px;top:257px;border-top:1px solid var(--line)}
.trusted-label{position:absolute;top:300px;width:100%;text-align:center;font-size:11.5px;letter-spacing:2px;color:#9aa3ae}
.trusted-brands{position:absolute;top:340px;width:100%;display:flex;justify-content:center;gap:58px;font-family:"Lexend",sans-serif;font-weight:700;font-size:18px;letter-spacing:1.5px;color:#c3cad4}
.legal{position:absolute;top:436px;left:44px;right:38px;display:flex;justify-content:space-between;font-size:11px;color:#4a4f57}
.legal nav{display:flex;gap:22px;color:#9aa3ae}
</style>
</head>
<body>

<header class="site-nav">
  <div class="brand"><span class="brand-square"></span>Rivet Athletic Supply</div>
  <nav class="nav-links"><span>Home</span><span>Locker Room</span><span>Custom Uniforms</span><span>Brands</span><span>About</span></nav>
  <a class="btn-primary nav-cta">Start Designing</a>
  <div class="cart">
    <svg width="16" height="16" viewBox="0 0 24 24"><path d="M6 8h12l-1 13H7z" fill="#111"/><path d="M9 8V6a3 3 0 0 1 6 0v2" fill="none" stroke="#111" stroke-width="2"/></svg>
  </div>
</header>

<section class="hero">
  <div class="hero-photo" role="img" aria-label="Football players in red and gold uniforms under stadium lights"></div>
  <div class="hero-shade"></div>
  <h1 class="hero-title heading">Design Your<br>Own.<br>Wear Your<br>Pride.</h1>
  <p class="hero-sub">Embark on your design journey: Select your sport, colors,<br>and upload your logo to visualize your team's custom gear.</p>

  <form class="design-card">
    <h2 class="heading">Your Design Journey<br>Starts Here</h2>
    <div class="field-label">1. Choose Your Sport</div>
    <div class="select"><span>Select a sport</span>
      <svg width="12" height="12" viewBox="0 0 12 12"><path d="M2 4l4 4 4-4" fill="none" stroke="#666" stroke-width="1.5"/></svg>
    </div>
    <div class="field-label">2. Select Your Basic Colors</div>
    <div class="colors">
      <span class="swatch"><i style="background:#1a1aff"></i>Primary</span>
      <span class="swatch"><i style="background:#fff;border:1px solid #bbb"></i>Secondary</span>
    </div>
    <div class="field-label">3. Upload Your Placeholder Logo</div>
    <div class="dropzone">
      <svg width="22" height="26" viewBox="0 0 22 26"><path d="M2 2h12l6 6v16H2z" fill="#8a95a6"/><path d="M11 19v-7M8 15l3-3 3 3" stroke="#fff" stroke-width="2" fill="none"/></svg>
      <span>Drag &amp; drop or click to upload</span>
    </div>
    <div class="drop-note">PNG, JPG, SVG up to 5MB</div>
    <a class="btn-primary card-cta">See My Design Recommendations</a>
  </form>
</section>

<section class="steps">
  <h2 class="section-title heading">How It Works: Your Next Steps</h2>
  <div class="step" style="left:64px">
    <div class="step-icon"><svg width="30" height="30" viewBox="0 0 24 24"><path d="M12 3a9 9 0 0 0 0 18c1.2 0 1.6-.9 1.2-1.8-.5-1 .2-2.2 1.4-2.2H17a4 4 0 0 0 4-4c0-5.5-4-10-9-10z" fill="var(--blue)"/><circle cx="7.5" cy="11" r="1.4" fill="#fff"/><circle cx="10" cy="7" r="1.4" fill="#fff"/><circle cx="14.5" cy="7" r="1.4" fill="#fff"/><circle cx="17" cy="11" r="1.4" fill="#fff"/></svg></div>
    <h3 class="heading">Refine Your Look</h3>
    <p>Adjust colors, add player names/numbers, and fine-tune your logo placement in our full customizer.</p>
  </div>
  <div class="step" style="left:450px">
    <div class="step-icon"><svg width="30" height="30" viewBox="0 0 24 24"><path d="M8 3l-5 3 2 5 2-1v11h10V10l2 1 2-5-5-3c-.5 1.5-2 2.5-4 2.5S8.5 4.5 8 3z" fill="var(--blue)"/></svg></div>
    <h3 class="heading">Explore Apparel Options</h3>
    <p>See your design on various jerseys, shorts, hoodies, and footwear for your chosen sport.</p>
  </div>
  <div class="step" style="left:835px">
    <div class="step-icon"><svg width="32" height="30" viewBox="0 0 26 24"><path d="M3 4l15 6-15 6 2-6z" fill="var(--blue)"/><circle cx="19" cy="16" r="5" fill="var(--blue)" stroke="#fff" stroke-width="1.5"/><path d="M17 16h4M19 14v4" stroke="#fff" stroke-width="1.5"/></svg></div>
    <h3 class="heading">Get Your Free Quote</h3>
    <p>Submit your design for a personalized quote and a professional proof from our team.</p>
  </div>
</section>

<section class="gear">
  <h2 class="heading">Popular Gear Based On Your Choices</h2>
  <a class="view-all">View all sports</a>
  <div class="gear-card tone-basketball" style="left:38px" role="img" aria-label="Basketball player dribbling in a white jersey"><span>Basketball Jerseys</span></div>
  <div class="gear-card tone-football" style="left:421px" role="img" aria-label="Football team in blue and gold uniforms"><span>Football Kits</span></div>
  <div class="gear-card tone-baseball" style="left:803px" role="img" aria-label="Baseball bat resting on jersey fabric"><span>Baseball Uniforms</span></div>
</section>

<section class="champions">
  <h2 class="section-title heading">Worn By Champions</h2>
  <p class="lead">Real teams, real games, real gear. Get inspired by the community.</p>
  <div class="gallery-tile t-basketball" style="left:38px;top:191px" role="img" aria-label="Basketball player leaping with the ball"><span class="tag">BASKETBALL</span></div>
  <div class="gallery-tile t-track" style="left:421px;top:191px" role="img" aria-label="Runner tying shoes on a track"><span class="tag">TRACK &amp; FIELD</span></div>
  <div class="gallery-tile t-hockey" style="left:803px;top:191px" role="img" aria-label="Hockey player skating with a stick"><span class="tag">HOCKEY</span></div>
  <div class="gallery-tile t-volleyball" style="left:38px;top:573px" role="img" aria-label="Volleyball team celebrating on court"><span class="tag">VOLLEYBALL</span></div>
  <div class="gallery-tile t-soccer" style="left:421px;top:573px" role="img" aria-label="Soccer player with a ball indoors"><span class="tag">SOCCER</span></div>
  <div class="gallery-tile t-baseball" style="left:803px;top:573px" role="img" aria-label="Baseball pitcher throwing from the mound"><span class="tag">BASEBALL</span></div>
  <a class="btn-outline">View Gallery &amp; Get Inspired</a>
</section>

<section class="team-band">
  <h2 class="heading">Ordering for a Team or League?</h2>
  <p>Get a dedicated rep, bulk pricing discounts, and free vector<br>design help from our pros.</p>
  <a class="btn-primary team-cta">Contact Team Sales</a>
</section>

<footer class="site-footer">
  <div class="brand footer-brand"><span class="brand-square"></span>Rivet Athletic Supply</div>
  <p class="footer-about">Empowering teams to look as good as they play. Quality custom apparel for every sport.</p>
  <div class="footer-col" style="left:328px"><h4>SHOP</h4><ul><li>Jerseys</li><li>Footwear</li><li>Accessories</li><li>Team Packs</li></ul></div>
  <div class="footer-col" style="left:618px"><h4>SUPPORT</h4><ul><li>Order Status</li><li>Sizing Charts</li><li>Contact Us</li><li>Returns</li></ul></div>
  <div class="footer-col" style="left:909px"><h4>STAY CONNECTED</h4>
    <div class="socials"><i style="background:#f3d6d6"></i><i style="background:#d8def0"></i><i style="background:#dde9f3"></i></div>
    <div class="phone">1-888-555-0147</div>
  </div>
  <div class="divider"></div>
  <div class="trusted-label">TRUSTED BRANDS WE USE</div>
  <div class="trusted-brands"><span>NORTHLINE</span><span>STRIDEFORM</span><span>IRONWEAVE</span><span>VICTOR MILL</span><span>KESTREL</span></div>
  <div class="legal"><span>© 2025 Rivet Athletic Supply. All rights reserved.</span><nav><span>Privacy Policy</span><span>Terms of Service</span></nav></div>
</footer>

</body>
</html>
```